Business Card, Stationary with Shark Logo for Personal Injury Lawyer

I need business cards and stationery with a shark logo for my Personal Injury Law Practice. Has to have this written on it:
Martin K. Hollis
Injury Lawyer
The Corvell Building
718 Tandy Street
Providence, Rhode Island 02908
401-627-4193
Martinhollis.com

Contact Information for Business Card

Martin K. Hollis, Injury Lawyer, address, 401-627-4193, martinhollis.com

```html
<!DOCTYPE html>
<html lang="en">
<head>
<meta charset="utf-8">
<title>Martin K. Hollis – Business Card</title>
<link href="https://fonts.googleapis.com/css2?family=Open+Sans:wght@300;400;700&display=swap" rel="stylesheet">
<style>
  :root {
    --navy: #26215f;
    --white: #ffffff;
    --paper: #f4f4f5;
    --swoosh: #e4e5e8;
    --yellow: #f2d21b;
    --icon: #8d8aa8;
    --muted: #c9c7dc;
    --backdrop: #e9e6e1;
  }
  * { margin: 0; padding: 0; box-sizing: border-box; }
  html, body { width: 1200px; height: 1024px; overflow: hidden; }
  body {
    background: var(--backdrop);
    font-family: "Open Sans", Arial, sans-serif;
    position: relative;
  }
  .card {
    position: absolute;
    left: 180px;
    width: 840px;
    height: 480px;
    overflow: hidden;
    box-shadow: 0 10px 26px rgba(0,0,0,0.18);
  }
  .card-front { top: 24px; background: var(--navy); display: flex; align-items: center; justify-content: center; }
  .card-back { top: 520px; background: var(--paper); display: flex; }

  .brand { display: flex; align-items: center; gap: 18px; position: relative; }
  .brand-mark { flex: none; border-radius: 50%; }
  .wordmark {
    font-family: "Open Sans", Arial, sans-serif;
    font-weight: 700;
    text-transform: uppercase;
    letter-spacing: 1px;
    line-height: 1;
    white-space: nowrap;
  }
  .card-front .wordmark { color: var(--white); font-size: 50px; }
  .card-front .brand-mark { width: 64px; height: 64px; background: var(--white); }

  .contact-panel {
    width: 46%;
    background: var(--navy);
    color: var(--white);
    padding: 92px 28px 0 60px;
  }
  .contact-name { font-weight: 400; font-size: 27px; letter-spacing: 1px; text-transform: uppercase; white-space: nowrap; }
  .contact-title { font-weight: 300; font-size: 21px; color: var(--muted); margin-top: 4px; }
  .accent-rule { width: 150px; height: 5px; background: var(--yellow); border-radius: 3px; margin: 20px 0 24px; }
  .contact-list { list-style: none; }
  .contact-list li { display: flex; align-items: flex-start; gap: 12px; font-size: 16px; font-weight: 300; line-height: 22px; margin-bottom: 9px; }
  .contact-icon { width: 22px; height: 22px; flex: none; }

  .logo-panel { position: relative; flex: 1; display: flex; align-items: center; justify-content: center; }
  .logo-swoosh { position: absolute; inset: 0; width: 100%; height: 100%; }
  .card-back .wordmark { color: var(--navy); font-size: 32px; }
  .card-back .brand { gap: 14px; }
  .card-back .brand-mark { width: 44px; height: 44px; background: var(--navy); }
</style>
</head>
<body>
  <section class="card card-front" aria-label="Business card front">
    <div class="brand">
      <span class="brand-mark" role="img" aria-label="Shark logo mark"></span>
      <div class="wordmark">Martin K. Hollis</div>
    </div>
  </section>

  <section class="card card-back" aria-label="Business card back">
    <div class="contact-panel">
      <div class="contact-name">Martin K. Hollis</div>
      <div class="contact-title">Injury Lawyer</div>
      <div class="accent-rule"></div>
      <ul class="contact-list">
        <li>
          <svg class="contact-icon" viewBox="0 0 22 22"><circle cx="11" cy="11" r="10" fill="var(--icon)"/><rect x="6" y="7.5" width="10" height="7" fill="none" stroke="var(--navy)" stroke-width="1.4"/><path d="M6 7.5 L11 11.5 L16 7.5" fill="none" stroke="var(--navy)" stroke-width="1.4"/></svg>
          <span>Martin@martinhollis.com</span>
        </li>
        <li>
          <svg class="contact-icon" viewBox="0 0 22 22"><circle cx="11" cy="11" r="10" fill="var(--icon)"/><circle cx="11" cy="11" r="5.5" fill="none" stroke="var(--navy)" stroke-width="1.4"/><path d="M5.5 11 H16.5 M11 5.5 C8 8.5 8 13.5 11 16.5 M11 5.5 C14 8.5 14 13.5 11 16.5" fill="none" stroke="var(--navy)" stroke-width="1.2"/></svg>
          <span>Martinhollis.com</span>
        </li>
        <li>
          <svg class="contact-icon" viewBox="0 0 22 22"><circle cx="11" cy="11" r="10" fill="var(--icon)"/><path d="M7.5 6 L9.5 6 L10.5 8.6 L9.2 9.6 C9.9 11 11 12.1 12.4 12.8 L13.4 11.5 L16 12.5 L16 14.5 C16 15.3 15.3 16 14.5 16 C10.4 15.7 6.3 11.6 6 7.5 C6 6.7 6.7 6 7.5 6 Z" fill="var(--navy)"/></svg>
          <span>401-627-4193</span>
        </li>
        <li>
          <svg class="contact-icon" viewBox="0 0 22 22"><circle cx="11" cy="11" r="10" fill="var(--icon)"/><path d="M11 5 C8.5 5 7 6.8 7 8.8 C7 11.6 11 16.5 11 16.5 C11 16.5 15 11.6 15 8.8 C15 6.8 13.5 5 11 5 Z" fill="var(--navy)"/><circle cx="11" cy="8.9" r="1.5" fill="var(--icon)"/></svg>
          <span>The Corvell Building<br>718 Tandy Street<br>Providence, Rhode Island 02908</span>
        </li>
      </ul>
    </div>
    <div class="logo-panel">
      <svg class="logo-swoosh" viewBox="0 0 454 480" preserveAspectRatio="none" aria-hidden="true">
        <path d="M0 0 H320 C300 160 220 300 0 430 Z" fill="var(--swoosh)"/>
      </svg>
      <div class="brand">
        <span class="brand-mark" role="img" aria-label="Shark logo mark"></span>
        <div class="wordmark">Martin K. Hollis</div>
      </div>
    </div>
  </section>
</body>
</html>
```